Question cards for team bonding

Back design of playing cards and front of each card is a question (text) and might have some artwork.

These cards will be "Crew spark deck" that would be ideal to use when starting new teams and when new team members arrive to "old" teams to have ready questions at hand and different games to play with these questions.

Questions are categorised into 3 categories that are how easy (or hard) the questions are. Easy questions are simple to answer where hard questions might require some thought to figure out what you want to tell about yourself.

Industry/Entity Type

Office Supply

Font styles to use
Sans Serif
Decorative

Colors
ec1f27
ffc214
f78f20
ffffff

Requirements
Must have
• Design on the back of all the cards, with the word "Crew Spark Deck"
• Design for the front of the card where each card has a text question like "If you had one wish" or "Little known fact that no one knows about you".
• There are three categories of questions: Easy, Medium and Hard, that I would like to have in different colour, i've been thinking easy = yellow cards, medium = orange cards and hard = red cards.
• Then there would be different "games" to play with the question, these would be in another colour (gray)
Nice to have
• Simple (flat) artwork on each question, i.e. "If you had one wish" would have an image of a lamp (based on zarimond).

```html
<!DOCTYPE html>
<html lang="en">
<head>
<meta charset="utf-8">
<title>Crew Spark Deck – card designs</title>
<link href="https://fonts.googleapis.com/css2?family=Fira+Sans+Condensed:wght@600&display=swap" rel="stylesheet">
<style>
  :root {
    --red: #ec1f27;
    --red-light: #ff5257;
    --red-dark: #c4161d;
    --yellow: #ffc214;
    --yellow-deep: #ffb400;
    --orange: #f78f20;
    --orange-edge: #f27a0c;
    --orange-light: #ffa545;
    --white: #ffffff;
    --footer-yellow: #ffcf4d;
    --footer-red: #f36a6f;
    --page: #ffffff;
  }
  * { box-sizing: border-box; margin: 0; padding: 0; }
  html, body {
    width: 876px; height: 1200px; overflow: hidden; background: var(--page);
  }
  .sheet { position: relative; width: 876px; height: 1200px; }

  .card { position: absolute; width: 417px; height: 582px; border-radius: 18px; overflow: hidden; }
  .card--tl { left: 13px; top: 11px; }
  .card--tr { left: 447px; top: 11px; }
  .card--bl { left: 13px; top: 606px; }
  .card--br { left: 447px; top: 606px; }

  /* Backs */
  .card-back { color: var(--white); }
  .card-back--orange { background: var(--orange-edge); }
  .card-back--red { background: var(--red); }
  .back-panel {
    position: absolute; left: 23px; right: 23px; top: 22px; bottom: 23px;
    border-radius: 16px;
    box-shadow: 0 0 0 1px rgba(0,0,0,0.12), 0 1px 4px rgba(0,0,0,0.18);
  }
  .card-back--orange .back-panel { background: radial-gradient(circle at 50% 52%, var(--orange-light) 0%, var(--orange) 45%, var(--orange-edge) 100%); }
  .card-back--red .back-panel { background: radial-gradient(circle at 50% 52%, var(--red-light) 0%, var(--red) 50%, #e81c24 100%); }

  .back-title {
    position: absolute; left: 0; right: 0; top: 158px;
    font-family: "Fira Sans Condensed", sans-serif; font-weight: 600;
    font-size: 72px; line-height: 93px; letter-spacing: 2px;
    text-align: center; color: var(--white);
  }
  .back-title span { display: block; }

  /* Fronts */
  .card-front { background: var(--white); border: 10px solid; border-radius: 20px; }
  .card-front--easy { border-color: var(--yellow); }
  .card-front--hard { border-color: var(--red); }
  .art {
    position: absolute; left: 50%; top: 48px; width: 218px; height: 218px;
    margin-left: -109px; border-radius: 50%;
  }
  .card-front--easy .art { background: linear-gradient(135deg, var(--yellow-deep) 55%, #e0a000 100%); }
  .card-front--hard .art { background: linear-gradient(135deg, var(--red) 55%, var(--red-dark) 100%); }
  .question {
    position: absolute;
    font-family: "Fira Sans Condensed", sans-serif; font-weight: 600;
    font-size: 35px; line-height: 50px; color: var(--white); text-align: center;
    border-radius: 16px;
  }
  .card-front--easy .question { top: 320px; left: 40px; width: 318px; height: 59px; line-height: 59px; background: var(--yellow-deep); }
  .card-front--hard .question { top: 320px; left: 38px; width: 322px; height: 110px; padding-top: 5px; background: var(--red); }

  .front-footer {
    position: absolute; left: 0; right: 0; bottom: 18px; height: 22px;
    font-family: "Fira Sans Condensed", sans-serif; font-weight: 600;
    font-size: 19px; line-height: 22px; letter-spacing: 1px; text-align: center;
  }
  .card-front--easy .front-footer { color: var(--footer-yellow); }
  .card-front--hard .front-footer { color: var(--footer-red); }
</style>
</head>
<body>
<main class="sheet">

  <section class="card card--tl card-back card-back--orange" aria-label="Card back, medium category">
    <div class="back-panel"></div>
    <h2 class="back-title"><span>CREW</span><span>SPARK</span><span>DECK</span></h2>
  </section>

  <section class="card card--tr card-back card-back--red" aria-label="Card back, hard category">
    <div class="back-panel"></div>
    <h2 class="back-title"><span>CREW</span><span>SPARK</span><span>DECK</span></h2>
  </section>

  <section class="card card--bl card-front card-front--easy" aria-label="Easy question card">
    <div class="art" role="img" aria-label="Flat artwork: wall clock with long shadow on a yellow circle"></div>
    <p class="question">Best time of day</p>
    <p class="front-footer">CREW SPARK DECK</p>
  </section>

  <section class="card card--br card-front card-front--hard" aria-label="Hard question card">
    <div class="art" role="img" aria-label="Flat artwork: white heart with a question mark on a red circle"></div>
    <p class="question">Can you describe<br>LOVE?</p>
    <p class="front-footer">CREW SPARK DECK</p>
  </section>

</main>
</body>
</html>
```